" O INSTITUTO TERAVUNDA foi idealizado a partir de um ideal de auxílio humanitário a famílias (com algum idoso) com condições de sobrevivência comprometidas devido a problemas de doença, seja ela física; psicológica ou mesmo social. “ Teravunda” significa “dono da coragem” e, apesar de seu principal mantenedor ser uma casa de culto de matriz africana (Dasilore Mitaku Fenjo Arupe),o Centro Cultural visa atender a famílias com idosos que estejam desestruturadas, devido a algum tipo de doença, indiferente a visão política, religiosa e/ou cultural. Acreditamos que o idoso incluído num contexto familiar, ou mesmo num asilo, não deve ser culpado por qualquer atitude de sua juventude. Quem de nós, em idade de produção e escolhas pode garantir estar tomando decisões acertadas para seu futuro? Normalmente são as doenças que comprometem o bem estar social: vícios em bebidas e/ou drogas; doenças patológicas e/ou psicológicas ou mesmo “doenças sociais” desestruturam as relações interpessoais afastando os idosos da realidade. "

```html
<!DOCTYPE html>
<html lang="pt-BR">
<head>
<meta charset="UTF-8">
<title>Instituto Teravunda</title>
<link rel="stylesheet" href="https://fonts.googleapis.com/css2?family=Open+Sans:wght@400;600;700&display=swap">
<style>
  :root {
    --brand-orange: #e0592a;
    --paper: #f4ece9;
    --photo-warm: #b98f80;
    --photo-grey: #9d918c;
    --white: #ffffff;
    --ink-shadow: rgba(60, 25, 15, 0.55);
  }
  * { margin: 0; padding: 0; box-sizing: border-box; }
  html, body { width: 1200px; height: 1200px; overflow: hidden; }
  body { font-family: "Open Sans", Arial, sans-serif; background: var(--paper); }

  .hero {
    position: relative;
    width: 1200px;
    height: 1200px;
    overflow: hidden;
  }
  .hero-photo {
    position: absolute;
    inset: 0;
    background:
      radial-gradient(ellipse 420px 560px at 1000px 420px, #e4dcd8 0%, rgba(228,220,216,0) 70%),
      radial-gradient(ellipse 380px 440px at 820px 640px, var(--photo-warm) 0%, rgba(185,143,128,0) 75%),
      radial-gradient(ellipse 300px 300px at 620px 520px, #d2ab9c 0%, rgba(210,171,156,0) 80%),
      linear-gradient(90deg, #f3ebe8 0%, #e8d3ca 40%, #c4a99e 65%, var(--photo-grey) 100%);
  }
  .hero-blobs { position: absolute; inset: 0; }
  .hero-shade {
    position: absolute;
    inset: 0;
    background: linear-gradient(180deg,
      rgba(70,30,20,0) 40%,
      rgba(70,30,20,0.38) 58%,
      rgba(70,30,20,0.48) 80%,
      rgba(70,30,20,0.42) 100%);
  }

  .site-header {
    position: absolute;
    top: 0; left: 0; right: 0;
    height: 180px;
    display: flex;
    align-items: center;
    justify-content: space-between;
    padding: 0 150px 0 180px;
  }
  .brand {
    display: flex;
    align-items: center;
    gap: 16px;
    color: var(--brand-orange);
    font-weight: 700;
    font-size: 38px;
    line-height: 1;
    letter-spacing: 0.5px;
  }
  .brand-dot {
    width: 44px; height: 44px;
    border-radius: 50%;
    background: var(--brand-orange);
  }
  .main-nav { display: flex; gap: 70px; }
  .main-nav a {
    color: var(--white);
    text-decoration: none;
    font-weight: 700;
    font-size: 22px;
    text-shadow: 0 1px 8px rgba(60,25,15,0.45);
  }

  .hero-copy {
    position: absolute;
    left: 100px; right: 100px;
    top: 680px;
    text-align: center;
    color: var(--white);
  }
  .hero-title {
    font-weight: 700;
    font-size: 54px;
    line-height: 1.3;
    text-shadow: 0 2px 4px var(--ink-shadow), 0 4px 22px var(--ink-shadow);
  }
  .hero-text {
    margin-top: 44px;
    font-weight: 600;
    font-size: 32px;
    line-height: 1.45;
    text-shadow: 0 1px 3px var(--ink-shadow), 0 2px 16px var(--ink-shadow);
  }
</style>
</head>
<body>
  <section class="hero">
    <div class="hero-photo" role="img" aria-label="Fotografia suave de uma pessoa idosa de cabelos brancos, em tons claros e rosados"></div>

    <svg class="hero-blobs" width="1200" height="1200" viewBox="0 0 1200 1200" aria-hidden="true">
      <path d="M0 0 H170 C240 120 230 300 150 420 C90 510 30 520 0 520 Z" fill="#f2d6cb" opacity="0.85"/>
      <path d="M0 520 C120 470 260 520 300 640 C340 760 260 900 120 960 C60 985 20 990 0 990 Z" fill="#f6e1d8" opacity="0.45"/>
      <path d="M330 230 C470 160 600 250 640 380 C690 540 560 640 430 600 C300 560 220 330 330 230 Z" fill="#f1cfc2" opacity="0.75"/>
      <path d="M560 660 C700 560 820 640 860 760 C900 880 760 960 640 920 C520 880 470 720 560 660 Z" fill="#e8bcac" opacity="0.35"/>
      <path d="M300 1200 C330 1060 480 1000 620 1040 C760 1080 800 1160 790 1200 Z" fill="#e9bfae" opacity="0.45"/>
      <path d="M0 1010 C70 990 150 1030 170 1110 C180 1160 170 1190 160 1200 H0 Z" fill="#efcdc0" opacity="0.5"/>
    </svg>
    <div class="hero-shade"></div>

    <header class="site-header">
      <div class="brand">
        <span class="brand-dot"></span>
        <span class="brand-name">Instituto Teravunda</span>
      </div>
      <nav class="main-nav">
        <a href="#">Home</a>
        <a href="#">Quem Somos</a>
      </nav>
    </header>

    <div class="hero-copy">
      <h1 class="hero-title">Quem de nós, em idade de produção e escolhas pode garantir estar tomando decisões acertadas para seu futuro?</h1>
      <p class="hero-text">Acreditamos que o idoso incluído num contexto familiar, ou mesmo num asilo, não deve ser culpado por qualquer atitude de sua juventude.</p>
    </div>
  </section>
</body>
</html>
```